Pages toward Inner Calm - book cover

12/18 update: Please read the entire brief. I don’t love anything that has been provided up to today. Please use the graphics and colors I’ve attached!!!! Show me your creations.

I am looking for a book cover design. It is a mental health journal. Needs to be very warm, inviting, calming. I’m very interested in new creative ideas. It will be wire-o bound and also in hard copy front and back. Use the graphic and colors I already have attached to this file. It’s called “Pages Toward Inner Calm”. Self means soul or spirit or center. The idea of integration may be a fit here in some way. If some words need to be emphasized in the design, “Self” and “QRM” would be the most important. size 6"x9". The words on the front can be smaller and more inviting then they would normally be on a fiction paperback.

Update 12/16: I am not excited about any of the submissions so far. I’m looking forward to seeing more options.

Target Market(s)

Adults 30-60. Male and female. People who like to learn. People wanting to heal. Middle and upper income.

Industry/Entity Type

Mental health. Wellness

Font styles to use
Other font styles liked:
• Whatever font is used in my logo. i don’t know the name. I also would be open to a different font if it was warm, inviting, and calm.

Colors
0094D4
00A9DD
6FCCEA
C7EBF8
E9F6FB

Requirements
Must have
• My logo colors. The words “Pages Toward Inner Calm” and “A 13-Week QRM Exploration”
Nice to have
• I’d like to see some creative ideas. More abstract than realistic.
Should not have
• No realist art or photos.

```html
<!DOCTYPE html>
<html lang="en">
<head>
<meta charset="utf-8">
<title>Pages toward Inner Calm – Cover</title>
<link rel="stylesheet" href="https://fonts.googleapis.com/css2?family=Montserrat:wght@300;400&display=swap">
<style>
  :root {
    --page-bg: #ffffff;
    --teal-deep: #04606c;
    --teal-mid: #0796a8;
    --teal-bright: #00bcd6;
    --teal-shadow: #035561;
    --ink-light: #f2f7f8;
  }
  * { margin: 0; padding: 0; box-sizing: border-box; }
  html, body {
    width: 1200px; height: 900px; overflow: hidden;
    background: var(--page-bg);
    font-family: "Montserrat", sans-serif;
  }
  .cover {
    position: absolute; left: 327px; top: 40px;
    width: 547px; height: 820px; overflow: hidden;
    background: var(--teal-mid);
    color: var(--ink-light);
  }
  .cover-waves { position: absolute; inset: 0; }
  .brand-seal {
    position: absolute; left: 33px; top: 89px;
    width: 140px; height: 140px; border-radius: 50%;
    background: var(--teal-deep);
    display: flex; align-items: center; justify-content: center;
    text-align: center;
    font-size: 14px; font-weight: 300; letter-spacing: 3px;
    text-transform: uppercase; line-height: 1.5;
  }
  .title { position: absolute; font-weight: 300; line-height: 1; white-space: nowrap; }
  .title-pages { top: 180px; left: 225px; font-size: 78px; }
  .title-toward { top: 268px; left: 128px; font-size: 40px; letter-spacing: -1px; }
  .title-calm { top: 318px; left: 118px; font-size: 128px; letter-spacing: 2px; }
  .subtitle {
    position: absolute; top: 450px; left: 124px;
    font-size: 27px; font-weight: 300; letter-spacing: -0.5px; white-space: nowrap;
  }
  .emblem-area { position: absolute; left: 190px; top: 495px; width: 205px; height: 140px; }
  .path-area { position: absolute; left: 150px; top: 580px; width: 420px; height: 260px; }
  .author {
    position: absolute; top: 718px; left: 128px;
    font-size: 26px; font-weight: 300; letter-spacing: 4px; white-space: nowrap;
  }
</style>
</head>
<body>
  <main class="cover">
    <svg class="cover-waves" viewBox="0 0 547 820" width="547" height="820" aria-hidden="true">
      <defs>
        <linearGradient id="cover-base" x1="0" y1="0" x2="1" y2="1">
          <stop offset="0" stop-color="#0a8d9d"/>
          <stop offset="0.5" stop-color="#0799ab"/>
          <stop offset="1" stop-color="#04707d"/>
        </linearGradient>
      </defs>
      <rect width="547" height="820" fill="url(#cover-base)"/>
      <path d="M180 0 C300 80 430 110 547 70 L547 0 Z" fill="var(--teal-bright)"/>
      <path d="M0 0 C120 60 220 210 547 170 L547 110 C420 150 300 90 170 0 Z" fill="#09a3b6" opacity="0.7"/>
      <path d="M0 240 C160 300 280 390 547 300 L547 360 C300 430 160 340 0 300 Z" fill="#0aaec2" opacity="0.45"/>
      <path d="M0 360 C200 420 330 460 547 430 L547 470 C330 500 180 450 0 400 Z" fill="#0ab3c6" opacity="0.35"/>
      <path d="M0 350 C120 420 200 520 330 640 L547 780 L547 820 L260 820 C200 700 100 560 0 480 Z" fill="var(--teal-deep)" opacity="0.55"/>
      <path d="M0 560 C100 620 180 720 240 820 L0 820 Z" fill="var(--teal-shadow)" opacity="0.5"/>
      <path d="M0 500 C110 560 190 660 270 820" fill="none" stroke="#0aa8bb" stroke-width="18" opacity="0.35"/>
    </svg>

    <div class="brand-seal">Lindqvist<br>Wellness</div>

    <h1>
      <span class="title title-pages">Pages</span>
      <span class="title title-toward">toward Inner</span>
      <span class="title title-calm">CALM</span>
    </h1>
    <p class="subtitle">A 13-Week QRM Exploration</p>

    <svg class="path-area" viewBox="0 0 420 260" role="img" aria-label="Illustration of a winding road leading up to the lotus">
      <defs>
        <radialGradient id="path-tone" cx="0.5" cy="0.5" r="0.5">
          <stop offset="0" stop-color="#03515c" stop-opacity="0.45"/>
          <stop offset="0.6" stop-color="#03515c" stop-opacity="0.2"/>
          <stop offset="1" stop-color="#03515c" stop-opacity="0"/>
        </radialGradient>
      </defs>
      <ellipse cx="210" cy="130" rx="210" ry="130" fill="url(#path-tone)"/>
    </svg>

    <svg class="emblem-area" viewBox="0 0 205 140" role="img" aria-label="Line drawing of a seated figure within a lotus flower">
      <defs>
        <radialGradient id="emblem-tone" cx="0.5" cy="0.5" r="0.5">
          <stop offset="0" stop-color="#3cbccb" stop-opacity="0.55"/>
          <stop offset="0.6" stop-color="#2aaebf" stop-opacity="0.25"/>
          <stop offset="1" stop-color="#0893a4" stop-opacity="0"/>
        </radialGradient>
      </defs>
      <ellipse cx="102.5" cy="70" rx="102.5" ry="70" fill="url(#emblem-tone)"/>
    </svg>

    <p class="author">LINDQVIST WELLNESS</p>
  </main>
</body>
</html>
```